Updated Stationary needed using new logo for Hair Tissue Mineral Analysis Company

Simple stationary design needed using new logo!
1. 8.5" x 11" Letterhead with company information listed below
2. 8.5" x 11" Design with Footer only with logo and information for print materials
3. 5.5" x 8.5" letterhead design
4. 4.125" x 9.5" Business envelope (#10 envelope) with address
5. 4.125" x 9.5" Business envelope with clear window (#10 envelope) with address
6. 6.5" x 9.5" envelope (6 3/4 Booklet envelope) with address
7. 10" x 13" Open End envelope
Address:
4817 N. Corwin Street
Phoenix, AZ 85021
Phone:
(602)-417-3926
Website:
www.pexumor.com
Email:
information@pexumor.com
Updates
Need extra days to review
Focused on completing other projects first
Look and feel
Each slider illustrates characteristics of the customer's brand and the style your logo design should communicate.

```html
<!DOCTYPE html>
<html lang="en">
<head>
<meta charset="utf-8">
<title>Pexumor Labs Stationery</title>
<link href="https://fonts.googleapis.com/css2?family=Montserrat:wght@400;600&family=Roboto:wght@400&display=swap" rel="stylesheet">
<style>
:root{
  --bg:#d3d4d6;
  --paper:#ffffff;
  --blue:#2d5aa0;
  --orange:#f08a24;
  --navy:#0c1838;
  --ink:#5a5f66;
  --brand:#2f5fae;
}
*{margin:0;padding:0;box-sizing:border-box}
html,body{width:1200px;height:1015px;overflow:hidden;background:var(--bg)}
body{position:relative;font-family:'Montserrat',sans-serif;color:var(--ink)}
.sheet{position:absolute;background:var(--paper);box-shadow:2px 3px 6px rgba(0,0,0,.28);overflow:hidden}
.footer-band{position:absolute;left:0;bottom:0;width:100%;background:var(--blue);border-top:3px solid var(--orange);display:flex;align-items:center;justify-content:center;color:#fff;font-family:'Montserrat',sans-serif;letter-spacing:.12em}
.brand{position:absolute;display:flex;align-items:center;gap:4px;font-family:'Montserrat',sans-serif;font-weight:600;color:var(--brand);white-space:nowrap}
.brand .dot{display:inline-block;border-radius:50%;background:var(--orange)}
.body-text{position:absolute;font-family:'Montserrat',sans-serif;color:var(--ink)}
.body-text p{margin-bottom:1.15em;line-height:1.55}
.sig{position:absolute;background:linear-gradient(90deg,#e9e9e9,#d4d4d4);border-radius:2px}
.rule{position:absolute;height:0;border-top:.6px solid #b9bcc0}
.foot-info{position:absolute;left:0;width:100%;text-align:center;font-family:'Roboto',sans-serif;color:var(--ink)}
.ic{color:var(--blue)}
.addr{position:absolute;font-family:'Roboto',sans-serif;color:var(--ink);line-height:1.25}
.addr .name{color:var(--brand)}
.window{position:absolute;border-radius:5px;background:linear-gradient(135deg,#d8d8d8 0%,#ececec 35%,#d0d0d0 55%,#e4e4e4 100%);border:1px solid #c4c4c4}
.flap{position:absolute;left:0;top:0;width:100%}
</style>
</head>
<body>

<section class="sheet letterhead-a" style="left:109px;top:92px;width:302px;height:426px">
  <div class="brand" style="left:31px;top:30px;font-size:11px"><span class="dot" style="width:7px;height:7px"></span>Pexumor Labs</div>
  <div class="addr" style="left:198px;top:22px;font-size:4.8px;line-height:1.6">
    4817 N. Corwin Street<br>Phoenix, AZ 85021<br>
    <span class="ic">&#9742;</span> (602)-417-3926<br>
    <span class="ic">&#9993;</span> information@pexumor.com
  </div>
  <div class="body-text" style="left:31px;top:100px;width:242px;font-size:4.4px">
    <p>Dear customer,</p>
    <p>Lorem ipsum dolor sit amet, consectetur adipisicing elit, sed do eiusmod tempor incididunt ut labore et dolore magna aliqua. Ut enim ad minim veniam, quis nostrud exercitation ullamco laboris nisi ut aliquip ex ea commodo consequat. Duis aute irure dolor in reprehenderit in voluptate velit esse cillum dolore eu fugiat nulla pariatur. Excepteur sint occaecat cupidatat non proident, sunt in culpa qui officia deserunt mollit anim id est laborum.</p>
    <p>Lorem ipsum dolor sit amet, consectetur adipisicing elit, sed do eiusmod tempor incididunt ut labore et dolore magna aliqua. Ut enim ad minim veniam, quis nostrud exercitation ullamco laboris nisi ut aliquip ex ea commodo consequat. Duis aute irure dolor in reprehenderit in voluptate velit esse cillum dolore eu fugiat nulla pariatur. Excepteur sint occaecat cupidatat non proident, sunt in culpa qui officia deserunt mollit anim id est laborum.</p>
    <p>Lorem ipsum dolor sit amet, consectetur adipisicing elit, sed do eiusmod tempor incididunt ut labore et dolore magna aliqua. Ut enim ad minim veniam, quis nostrud exercitation ullamco laboris nisi ut aliquip ex ea commodo consequat. Duis aute irure dolor in reprehenderit in voluptate velit esse cillum dolore eu fugiat nulla pariatur. Excepteur sint occaecat cupidatat non proident, sunt in culpa qui officia deserunt mollit anim id est laborum.</p>
    <p>Lorem ipsum dolor sit amet, consectetur adipisicing elit, sed do eiusmod tempor incididunt ut labore et dolore magna aliqua. Ut enim ad minim veniam, quis nostrud exercitation ullamco laboris nisi ut aliquip ex ea commodo consequat. Duis aute irure dolor in reprehenderit.</p>
    <p>Yours Sincerely,</p>
    <p style="margin-top:1.6em">Mark Dalen<br>General Director</p>
  </div>
  <div class="sig" role="img" aria-label="Handwritten signature" style="left:31px;top:312px;width:30px;height:22px"></div>
  <div class="footer-band" style="height:20px;font-size:6.5px">www.pexumor.com</div>
</section>

<section class="sheet letterhead-b" style="left:434px;top:92px;width:302px;height:426px">
  <div class="brand" style="left:78px;top:22px;font-size:13.5px"><span class="dot" style="width:9px;height:9px"></span>Pexumor Labs</div>
  <div class="body-text" style="left:31px;top:100px;width:242px;font-size:4.4px">
    <p>Dear customer,</p>
    <p>Lorem ipsum dolor sit amet, consectetur adipisicing elit, sed do eiusmod tempor incididunt ut labore et dolore magna aliqua. Ut enim ad minim veniam, quis nostrud exercitation ullamco laboris nisi ut aliquip ex ea commodo consequat. Duis aute irure dolor in reprehenderit in voluptate velit esse cillum dolore eu fugiat nulla pariatur. Excepteur sint occaecat cupidatat non proident, sunt in culpa qui officia deserunt mollit anim id est laborum.</p>
    <p>Lorem ipsum dolor sit amet, consectetur adipisicing elit, sed do eiusmod tempor incididunt ut labore et dolore magna aliqua. Ut enim ad minim veniam, quis nostrud exercitation ullamco laboris nisi ut aliquip ex ea commodo consequat. Duis aute irure dolor in reprehenderit in voluptate velit esse cillum dolore eu fugiat nulla pariatur. Excepteur sint occaecat cupidatat non proident, sunt in culpa qui officia deserunt mollit anim id est laborum.</p>
    <p>Lorem ipsum dolor sit amet, consectetur adipisicing elit, sed do eiusmod tempor incididunt ut labore et dolore magna aliqua. Ut enim ad minim veniam, quis nostrud exercitation ullamco laboris nisi ut aliquip ex ea commodo consequat. Duis aute irure dolor in reprehenderit in voluptate velit esse cillum dolore eu fugiat nulla pariatur. Excepteur sint occaecat cupidatat non proident, sunt in culpa qui officia deserunt mollit anim id est laborum.</p>
    <p>Lorem ipsum dolor sit amet, consectetur adipisicing elit, sed do eiusmod tempor incididunt ut labore et dolore magna aliqua. Ut enim ad minim veniam, quis nostrud exercitation ullamco laboris nisi ut aliquip ex ea commodo consequat. Duis aute irure dolor in reprehenderit.</p>
    <p>Yours Sincerely,</p>
    <p style="margin-top:1.6em">Mark Dalen<br>General Director</p>
  </div>
  <div class="sig" role="img" aria-label="Handwritten signature" style="left:31px;top:312px;width:30px;height:22px"></div>
  <div class="rule" style="left:31px;width:240px;top:381px"></div>
  <div class="foot-info" style="top:390px;font-size:6px">4817 N. Corwin Street Phoenix, AZ 85021</div>
  <div class="foot-info" style="top:400px;font-size:6px"><span class="ic">&#9742;</span> (602)-417-3926 &nbsp;<span class="ic">&#9993;</span> information@pexumor.com &nbsp;<span class="ic">&#9673;</span> www.pexumor.com</div>
</section>

<section class="sheet letterhead-c" style="left:758px;top:151px;width:237px;height:367px">
  <div class="brand" style="left:62px;top:22px;font-size:10px"><span class="dot" style="width:7px;height:7px"></span>Pexumor Labs</div>
  <div class="body-text" style="left:26px;top:91px;width:186px;font-size:3.2px">
    <p>Dear customer,</p>
    <p>Lorem ipsum dolor sit amet, consectetur adipisicing elit, sed do eiusmod tempor incididunt ut labore et dolore magna aliqua. Ut enim ad minim veniam, quis nostrud exercitation ullamco laboris nisi ut aliquip ex ea commodo consequat. Duis aute irure dolor in reprehenderit in voluptate velit esse cillum dolore eu fugiat nulla pariatur. Excepteur sint occaecat cupidatat non proident, sunt in culpa qui officia deserunt mollit anim id est laborum.</p>
    <p>Lorem ipsum dolor sit amet, consectetur adipisicing elit, sed do eiusmod tempor incididunt ut labore et dolore magna aliqua. Ut enim ad minim veniam, quis nostrud exercitation ullamco laboris nisi ut aliquip ex ea commodo consequat. Duis aute irure dolor in reprehenderit in voluptate velit esse cillum dolore eu fugiat nulla pariatur. Excepteur sint occaecat cupidatat non proident, sunt in culpa qui officia deserunt mollit anim id est laborum.</p>
    <p>Lorem ipsum dolor sit amet, consectetur adipisicing elit, sed do eiusmod tempor incididunt ut labore et dolore magna aliqua. Ut enim ad minim veniam, quis nostrud exercitation ullamco laboris nisi ut aliquip ex ea commodo consequat. Duis aute irure dolor in reprehenderit in voluptate velit esse cillum dolore eu fugiat nulla pariatur. Excepteur sint occaecat cupidatat non proident, sunt in culpa qui officia deserunt mollit anim id est laborum.</p>
    <p>Lorem ipsum dolor sit amet, consectetur adipisicing elit, sed do eiusmod tempor incididunt ut labore et dolore magna aliqua. Ut enim ad minim veniam, quis nostrud exercitation ullamco laboris nisi ut aliquip ex ea commodo consequat. Duis aute irure dolor in reprehenderit.</p>
    <p>Yours Sincerely,</p>
    <p style="margin-top:1.6em">Mark Dalen<br>General Director</p>
  </div>
  <div class="sig" role="img" aria-label="Handwritten signature" style="left:26px;top:254px;width:24px;height:18px"></div>
  <div class="rule" style="left:17px;width:203px;top:335px"></div>
  <div class="foot-info" style="top:343px;font-size:4.6px">4817 N. Corwin Street Phoenix, AZ 85021</div>
  <div class="foot-info" style="top:351px;font-size:4.6px"><span class="ic">&#9742;</span> (602)-417-3926 &nbsp;<span class="ic">&#9993;</span> information@pexumor.com &nbsp;<span class="ic">&#9673;</span> www.pexumor.com</div>
</section>

<section class="sheet envelope-flap" style="left:109px;top:542px;width:339px;height:158px">
  <svg class="flap" viewBox="0 0 339 58" style="height:58px">
    <path d="M0 0 H339 L303 50 Q298 58 288 58 H51 Q41 58 36 50 Z" fill="var(--navy)"/>
  </svg>
  <div class="brand" style="left:96px;top:20px;font-size:13px"><span class="dot" style="width:8px;height:8px"></span>Pexumor Labs</div>
</section>

<section class="sheet envelope-window" style="left:469px;top:542px;width:340px;height:158px">
  <div class="addr" style="left:26px;top:20px;font-size:7px">
    <span class="name">Pexumor Labs, Inc</span><br>4817 N. Corwin Street<br>Phoenix, AZ 85021
  </div>
  <div class="window" style="left:26px;top:86px;width:126px;height:35px"></div>
  <div class="footer-band" style="height:20px;font-size:7px">www.pexumor.com</div>
</section>

<section class="sheet booklet-a" style="left:826px;top:542px;width:267px;height:182px">
  <div class="addr" style="left:21px;top:19px;font-size:7px">
    <span class="name">Pexumor Labs, Inc</span><br>4817 N. Corwin Street<br>Phoenix, AZ 85021
  </div>
  <div class="footer-band" style="height:16px;font-size:5.5px">www.pexumor.com</div>
</section>

<section class="sheet envelope-plain" style="left:109px;top:712px;width:339px;height:158px">
  <div class="addr" style="left:25px;top:22px;font-size:7px">
    <span class="name">Pexumor Labs, Inc</span><br>4817 N. Corwin Street<br>Phoenix, AZ 85021
  </div>
  <div class="footer-band" style="height:20px;font-size:7px">www.pexumor.com</div>
</section>

<section class="sheet envelope-brand" style="left:469px;top:712px;width:340px;height:158px">
  <div class="brand" style="left:25px;top:18px;font-size:10px"><span class="dot" style="width:7px;height:7px"></span>Pexumor Labs</div>
  <div class="addr" style="left:25px;top:36px;font-size:6.5px">4817 N. Corwin Street<br>Phoenix, AZ 85021</div>
  <div class="footer-band" style="height:20px;font-size:7px">www.pexumor.com</div>
</section>

<section class="sheet booklet-b" style="left:826px;top:742px;width:267px;height:182px">
  <div class="brand" style="left:25px;top:20px;font-size:10px"><span class="dot" style="width:7px;height:7px"></span>Pexumor Labs</div>
  <div class="addr" style="left:25px;top:38px;font-size:6.5px">4817 N. Corwin Street<br>Phoenix, AZ 85021</div>
  <div class="footer-band" style="height:16px;font-size:5.5px">www.pexumor.com</div>
</section>

</body>
</html>
```